Publisher needs a book cover design for ‘Lanterns Over the Marsh Gate’ book

We need a book cover (front, back, spine) for the 2nd edition of a book entitled ‘Lanterns Over the Marsh Gate’ and subtitled ‘the quiet geography of tidal winds, ferry routes and harbour lanterns’ (inverted commas not to be part of the title and subtitle). The author is Rupert Calloway. The publisher is Vellmark Press. The finished size of the paperback version will be the industry standard 9" x 6". There will be paperback, hardback, and e-book versions. The final number of pages is expected to be in the region 150-180 pages. Text for the back cover is not yet available, but at the bottom of the back cover should be publisher logo (rectangular) on the left and space for the ISBN bar code on the right. The circular logo should be on the spine. The design should be original and not include any stock images that have been created by someone else or may require obtaining a copyright licence to use. Symbols in common use and not copyrighted are probably ok. There are no required images, photographs or symbols except the publisher logo at the left bottom of the back cover and lower spine. Spine lettering should be UK/US style with the top of the writing nearest the front cover. The designer is free to be creative using appropriate diagrams, symbols or abstract designs. Rectangular and circular variants of the publisher logo are attached. Designers are assured that when evaluating designs absolutely no notice whatsoever is taken of a designer's Pixo Rally ranking or status; We are completely output driven, so what matters is the design, not the ranking or status of the designer. In a similar way, designs are not evaluated as 'good' or 'bad' - the winning design will be chosen after review by a design review panel and is not decided arbitrarily by a single person. All submitted designs should be capable of effective copyright assignment.

Target Market(s)

Practitioners, parents, teachers, pupils and academics concerned with child protection, safeguarding and the elimination of emotional abuse of children in the classroom

Font styles to use
Serif
Sans Serif

Requirements
Must have
• • Title, author, edition, subtitle, publisher logo
Nice to have
• • Originality, innovation
Should not have
• • Stock images or anything else requiring additional copyright discussions and negotiations.

```html
<!DOCTYPE html>
<html lang="en">
<head>
<meta charset="utf-8">
<title>Lanterns Over the Marsh Gate — Cover Spread</title>
<link rel="stylesheet" href="https://fonts.googleapis.com/css2?family=Crimson+Pro:wght@400;500;600;700&family=Marcellus&display=swap">
<style>
  :root {
    --stage: #454545;
    --paper: #ffffff;
    --ink: #434343;
    --ink-soft: #3a3a3a;
    --blue: #3a63a6;
    --yellow: #f1c84c;
    --green: #45c445;
    --red: #c8344a;
  }
  * { margin: 0; padding: 0; box-sizing: border-box; }
  html, body { width: 1200px; height: 871px; overflow: hidden; background: var(--stage); }
  .spread {
    position: absolute; left: 82px; top: 56px; width: 1044px; height: 757px;
    background: var(--paper); color: var(--ink);
    font-family: "Crimson Pro", Georgia, serif;
  }
  .panel { position: absolute; top: 0; height: 100%; }
  .back { left: 0; width: 500px; }
  .spine { left: 500px; width: 48px; }
  .front { left: 548px; width: 496px; }

  .title {
    text-align: center; text-transform: uppercase; line-height: 1;
    font-family: "Crimson Pro", Georgia, serif; font-weight: 500;
  }
  .title .line { display: block; }
  .title .joiner { display: flex; align-items: center; justify-content: center; }
  .title .joiner::before, .title .joiner::after {
    content: ""; display: block; height: 1.5px; background: var(--ink);
  }
  .subtitle {
    text-align: center; text-transform: uppercase;
    font-family: "Marcellus", Georgia, serif; letter-spacing: .06em;
  }
  .edition { text-align: center; text-transform: uppercase; font-size: 11px; letter-spacing: .03em; color: var(--ink-soft); }

  /* back */
  .back .title { position: absolute; left: 0; width: 100%; top: 56px; }
  .back .title .big { font-size: 30px; }
  .back .title .joiner { font-size: 20px; margin: 3px 0 2px; }
  .back .title .joiner::before, .back .title .joiner::after { width: 52px; margin: 0 4px; height: 1px; }
  .back .title .huge { font-size: 34px; }
  .back .subtitle { position: absolute; top: 152px; left: 0; width: 100%; font-size: 11px; line-height: 14px; }
  .blurb { position: absolute; left: 38px; width: 422px; top: 228px; font-size: 14px; line-height: 19px; text-align: justify; color: var(--ink-soft); }
  .blurb p { text-indent: 8px; margin-bottom: 5px; }
  .back .edition { position: absolute; top: 488px; left: 0; width: 100%; }
  .back .swatch { left: 190px; top: 512px; width: 104px; height: 104px; opacity: .35; }
  .imprint { position: absolute; left: 26px; top: 678px; display: flex; align-items: center; gap: 4px; font-size: 15px; font-weight: 600; color: #222; letter-spacing: .02em; }
  .imprint .mark { width: 26px; height: 26px; border-radius: 50%; background: #222; }

  /* spine */
  .spine-text { position: absolute; left: 0; width: 100%; writing-mode: vertical-rl; display: flex; align-items: center; text-transform: uppercase; }
  .spine-title { top: 24px; height: 460px; font-size: 23px; line-height: 48px; }
  .spine-author { top: 516px; height: 176px; font-size: 16px; line-height: 48px; }
  .spine-mark { position: absolute; left: 14px; top: 710px; width: 20px; height: 20px; border-radius: 50%; border: 2px solid #222; }

  /* front */
  .front .edition { position: absolute; top: 34px; left: 0; width: 100%; font-size: 14px; }
  .front .title { position: absolute; top: 104px; left: 0; width: 100%; font-weight: 600; }
  .front .title .big { font-size: 54px; }
  .front .title .joiner { font-size: 38px; margin: 6px 0 4px; }
  .front .title .joiner::before, .front .title .joiner::after { width: 90px; margin: 0 6px; }
  .front .title .huge { font-size: 62px; }
  .front .subtitle { position: absolute; top: 272px; left: 0; width: 100%; font-size: 19px; line-height: 24px; }
  .front .swatch { left: 118px; top: 408px; width: 244px; height: 236px; }
  .author { position: absolute; top: 684px; left: 0; width: 100%; text-align: center; text-transform: uppercase; font-size: 29px; font-weight: 600; }

  .swatch {
    position: absolute; border-radius: 50%;
    background: linear-gradient(135deg, var(--blue), var(--yellow) 40%, var(--red) 70%, var(--green));
    opacity: .85;
  }
</style>
</head>
<body>
  <div class="spread">
    <section class="panel back">
      <h2 class="title">
        <span class="line big">Lanterns</span>
        <span class="line joiner">Over the</span>
        <span class="line huge">Marsh Gate</span>
      </h2>
      <p class="subtitle">The quiet geography<br>of tidal winds, ferry routes<br>and harbour lanterns</p>
      <div class="blurb">
        <p>Lorem ipsum dolor sit amet, consectetur adipiscing elit. Ut condimentum elit non tincidunt suscipit. Cras et felis a elit maximus vestibulum. Curabitur tincidunt, lectus sed cursus fringilla, leo purus posuere dolor, a ullamcorper ante tellus vitae lorem. Vestibulum porta viverra tellus a hendrerit. Donec porttitor arcu viverra justo gravida, et fringilla arcu egestas.</p>
        <p>Aliquam venenatis consectetur tortor. Donec hendrerit a dui id blandit. Fusce a auctor eros, ac congue sem. Suspendisse quis eros elementum, convallis augue sit amet, cursus augue. Mauris sed magna tortor. Integer nec pretium massa, ut lacinia justo. Etiam vitae malesuada mauris. In nulla urna, volutpat in sagittis vel, consequat at turpis. Class aptent taciti sociosqu ad litora torquent per conubia nostra, per inceptos himenaeos. Vestibulum bibendum id velit ac feugiat.</p>
      </div>
      <p class="edition">Second Edition</p>
      <div class="swatch" role="img" aria-label="Faint abstract colour artwork in blue, yellow, green and red"></div>
      <div class="imprint"><span class="mark"></span><span>VELLMARK PRESS</span></div>
    </section>

    <section class="panel spine">
      <div class="spine-text spine-title">Lanterns Over the Marsh Gate</div>
      <div class="spine-text spine-author">Rupert Calloway</div>
      <div class="spine-mark" aria-label="Vellmark Press"></div>
    </section>

    <section class="panel front">
      <p class="edition">Second Edition</p>
      <h1 class="title">
        <span class="line big">Lanterns</span>
        <span class="line joiner">Over the</span>
        <span class="line huge">Marsh Gate</span>
      </h1>
      <p class="subtitle">The quiet geography<br>of tidal winds, ferry routes<br>and harbour lanterns</p>
      <div class="swatch" role="img" aria-label="Abstract colour artwork in blue, yellow, green and red"></div>
      <p class="author">Rupert Calloway</p>
    </section>
  </div>
</body>
</html>
```